REALTOR/REALESTATE INVESTOR CARD

I AM MY LOCAL CITIES FLIP THIS HOUSE KING...I CHANGE NEIGHBORHOODS ONE HOUSE AT A TIME. I BUY OLD HOUSES FOR CASH TOTALLY RENOVATE THEM TO LIKE NEW, THEN RE SELL THEM...
I HAVE BEEN USING PLATINUM & BURGANDY AS MY MAIN COLOR..
I WANT SOMETHING FUN AND MODERN TO APPEAL TO ALL BUYERS AND SELLERS. AND TO REFLECT I AM AT THE TOP OF MY GAME...A WOW...THIS IS A GREAT CARD.......WOW.......I AM A REALTOR....I FLIP HOUSES.....MAYBE SHOW AND OLD HOUSE AND THEN A SPARKLING NEW HOUSE..... MY COMPANY NAME IS HOMESTEAD CAPITAL PARTNERS THE ADDRESS IS P.O.BOX 86 GOOSE CREEK, S.C. 29401

Target Market(s)

I SELL HOUSES THAT HAVE BEEN RENOVATED TO ALMOST BRAND NEW CONDITION.......I ALSO BUY HOUSES/MOBILES FOR ALL CASH FAST CLOSINGS..
I BUY GOOSE CREEK HOUSES ALL CASH FAST CLOSE.....I BUY MOBILE HOMES ANY CONDITION, ANY PRICE.....Buyers & sellers of houses.....

Industry/Entity Type

Investment

Font styles to use
Sans Serif

Requirements
Must have
• I BUY GOOSE CREEK HOUSES ALL CASH FAST CLOSINGS......
CHANGING GOOSE CREEK, ONE HOUSE AT A TIME...
RAY T. BELLAMY CIAS
REALTOR/CERTIFIED INVESTOR AGENT
HOMESTEAD CAPITAL PARTNERS,LLC.
P.O. BOX 86
GOOSE CREEK, S.C. 29401
843-555-0172
RAYBELLAMYHOUSES@QUILLMAIL.EXAMPLE
Nice to have
• GOOSE CREEK'S RE-HAB KING....
A actual picture of MAYBE A HOME BEING RENOVATED
TO ONE LOOKING AWESOME.....artwork
Should not have
• a picture of and old ugly home the a sparkling brand new one that is what I di I renovate homes.......

```html
<!DOCTYPE html>
<html lang="en">
<head>
<meta charset="utf-8">
<title>Homestead Capital Partners – Business Card</title>
<link rel="stylesheet" href="https://fonts.googleapis.com/css2?family=Cinzel:wght@400;500&family=EB+Garamond:ital@1&display=swap">
<style>
  :root {
    --backdrop: #e9e6e1;
    --card-white: #f4f4f4;
    --card-charcoal: #3c3c3e;
    --ink: #2c2c2c;
    --ink-light: #f2f2f2;
    --band: #3a3a3c;
  }
  * { margin: 0; padding: 0; box-sizing: border-box; }
  html, body { width: 1200px; height: 617px; overflow: hidden; }
  body {
    background: var(--backdrop);
    display: flex;
    align-items: center;
    justify-content: center;
    gap: 60px;
  }
  .card {
    width: 520px;
    height: 297px;
    position: relative;
    box-shadow: 0 6px 18px rgba(0,0,0,0.18);
  }
  /* Front */
  .card-front {
    background: var(--card-white);
    color: var(--ink);
    font-family: "Cinzel", "Times New Roman", serif;
    padding: 26px 30px 22px 54px;
    display: flex;
    flex-direction: column;
  }
  .card-front .edge-band {
    position: absolute;
    left: 0; top: 0; bottom: 0;
    width: 18px;
    background: var(--band);
  }
  .title {
    font-size: 20px;
    font-weight: 400;
    line-height: 1.08;
    letter-spacing: 0.2px;
  }
  .contact-list {
    list-style: none;
    margin-top: 30px;
    margin-left: 22px;
    font-size: 13px;
    line-height: 1.32;
  }
  .contact-list li { display: flex; align-items: center; gap: 6px; }
  .contact-list .no-icon { padding-left: 18px; }
  .contact-list svg { width: 12px; height: 12px; flex: none; }
  .tagline {
    margin-top: 6px;
    margin-left: 22px;
    font-size: 13px;
    line-height: 1.32;
  }
  /* Back */
  .card-back {
    background: var(--card-charcoal);
    color: var(--ink-light);
    font-family: "EB Garamond", Georgia, serif;
    font-style: italic;
    text-transform: uppercase;
    text-align: center;
    padding-top: 58px;
    font-size: 13px;
    line-height: 1.3;
    letter-spacing: 0.3px;
  }
</style>
</head>
<body>

  <section class="card card-front" aria-label="Card front">
    <div class="edge-band"></div>
    <h1 class="title">REALTOR/CERTIFIED INVESTOR AGENT<br>HOMESTEAD CAPITAL PARTNERS,LLC</h1>
    <ul class="contact-list">
      <li>
        <svg viewBox="0 0 12 12" aria-hidden="true"><path d="M6 1 L11 5.5 H9.5 V11 H2.5 V5.5 H1 Z" fill="currentColor"/></svg>
        P.O. BOX 86
      </li>
      <li>
        <svg viewBox="0 0 12 12" aria-hidden="true"><path d="M6 0.8 A4 4 0 0 1 10 4.8 C10 7.6 6 11.2 6 11.2 C6 11.2 2 7.6 2 4.8 A4 4 0 0 1 6 0.8 Z" fill="none" stroke="currentColor" stroke-width="1.3"/><circle cx="6" cy="4.8" r="1.4" fill="currentColor"/></svg>
        GOOSE CREEK, S.C. 29401
      </li>
      <li class="no-icon">843-555-0172</li>
      <li>
        <svg viewBox="0 0 12 12" aria-hidden="true"><rect x="0.5" y="0.5" width="11" height="11" rx="1.5" fill="currentColor"/><path d="M2.5 4 L6 6.6 L9.5 4 M2.5 4 V8.5 H9.5 V4" fill="none" stroke="#f4f4f4" stroke-width="1"/></svg>
        RAYBELLAMYHOUSES@QUILLMAIL.EXAMPLE
      </li>
    </ul>
    <p class="tagline">GOOSE CREEK'S RE-HAB KING....<br>MAYBE A HOME BEING RENOVATED<br>TO ONE LOOKING AWESOME.....</p>
  </section>

  <section class="card card-back" aria-label="Card back">
    <p>I buy Goose Creek houses all cash fast closings......<br>
    Changing Goose Creek, one house at a time...<br>
    Ray T. Bellamy CIAS</p>
  </section>

</body>
</html>
```